Make a medical leaflet for my patients undergoing ankle blocks

I have a very boring text only leaflet I would like to turn into a professional appealing medical leaflet to give to my patients. I would like to get this onto two pages of a4 if possible and its intended for electronic distribution mainly.
This will be for patients so it must be professional.
It must also contain a copyright logo on it and my name near the start (Dr Tobias Wendell) so my colleagues can't use it easily.
Target Market(s)
Patients undergoing surgery
Industry/Entity Type
Medical
Font styles to use
Other font styles liked:
- no idea, you tell me
Requirements
Must have
- the information contained on the attachment
- look professional
- a copyright on it
Nice to have
- the ashbury clinic logo
Should not have
- Any spelling, grammatical or linguistic errors
- Any font less than size 12

```html
<!DOCTYPE html>
<html lang="en">
<head>
<meta charset="utf-8">
<title>Ankle Block Patient Leaflet – Dr Tobias Wendell</title>
<link rel="stylesheet" href="https://fonts.googleapis.com/css2?family=Open+Sans:wght@400;600;700&display=swap">
<style>
:root{
  --brand-blue:#1d5a9c;
  --brand-blue-dark:#173f73;
  --ink:#2b2b2b;
  --grey-bar:#5f6368;
  --grey-panel:#6b6e72;
  --page:#ffffff;
  --backdrop:#e6e8eb;
}
*{box-sizing:border-box;margin:0;padding:0}
html,body{width:1200px;height:800px;overflow:hidden;background:var(--backdrop)}
body{font-family:"Open Sans",Arial,sans-serif;color:var(--ink);position:relative}
.page{position:absolute;top:18px;width:540px;height:764px;background:var(--page);overflow:hidden;box-shadow:0 2px 10px rgba(0,0,0,.18)}
.page--procedure{left:45px}
.page--overview{left:615px}
.abs{position:absolute}
.pill{position:absolute;height:22px;background:var(--brand-blue);color:#fff;font-weight:700;font-size:11.5px;letter-spacing:.6px;display:flex;align-items:center;border-radius:0 12px 12px 0;padding-left:22px}
.pill--round{border-radius:12px;justify-content:center;padding-left:0}
.copy{font-size:9px;line-height:1.32}
.copy p{margin-bottom:3px;text-align:justify}
.bullets{list-style:none}
.bullets li{position:relative;padding-left:10px;margin-bottom:1px}
.bullets li::before{content:"•";position:absolute;left:0}
.choice-bar{position:absolute;height:24px;background:var(--grey-bar);color:#fff;font-size:8.6px;line-height:1.15;text-align:center;display:flex;align-items:center;justify-content:center}
.vs-badge{position:absolute;width:38px;height:38px;border-radius:50%;background:var(--brand-blue);border:3px solid #fff;color:#fff;font-weight:700;font-size:14px;display:flex;align-items:center;justify-content:center;box-shadow:0 0 0 1px var(--brand-blue)}
.hospital-name{position:absolute;right:26px;top:20px;text-align:right;color:var(--brand-blue-dark);font-size:12.5px;font-weight:600}
.hospital-name small{display:block;font-size:7.5px;font-weight:400;color:var(--brand-blue)}
.footer{position:absolute;left:0;right:0;bottom:0;height:64px;background:var(--brand-blue);color:#fff;font-size:11px;display:flex;align-items:center;padding-left:32px}
.anatomy-visual{position:absolute;left:300px;top:455px;width:260px;height:260px;border-radius:50%;background:radial-gradient(circle at 38% 48%,#f08a2c 0,#c8461c 14%,#1f5fb5 38%,#0c2f6e 70%,#061a42 100%)}
.hero-photo{position:absolute;left:0;top:0;width:540px;height:170px;background:linear-gradient(90deg,#cfd2d6 0%,#9a9ea3 40%,#b05a4c 52%,#8d9196 62%,#d6d8db 100%)}
.clinic-mark{position:absolute;right:22px;top:0;width:138px;height:128px;background:var(--brand-blue);color:#fff;display:flex;flex-direction:column;align-items:center;justify-content:center;gap:8px;font-size:13px;font-weight:400;letter-spacing:3px;text-align:center;line-height:1.3}
.clinic-mark .square{width:9px;height:9px;background:#fff}
.benefits{position:absolute;left:22px;top:448px;width:238px;height:222px;background:linear-gradient(180deg,#7a7d81,#5b5e62)}
.benefits h3{height:24px;background:var(--brand-blue);color:#fff;font-size:11px;letter-spacing:.6px;font-weight:700;text-align:center;line-height:24px}
.benefits ol{list-style:none;color:#fff;padding:8px 12px;font-size:9px;line-height:1.3}
.benefits li{margin-bottom:3px}
.risk-heading{font-weight:700;margin-top:6px}
</style>
</head>
<body>

<section class="page page--procedure">
  <div class="pill" style="left:0;top:26px;width:240px">HOW IS IT DONE</div>
  <div class="hospital-name">Riverside Gate Hospital<small>part of Meridian Care UK</small></div>

  <div class="choice-bar" style="left:22px;top:58px;width:220px">If you choose awake surgery<br>or surgery with sedation</div>
  <div class="vs-badge" style="left:244px;top:51px">VS</div>
  <div class="choice-bar" style="left:284px;top:58px;width:236px">If you choose a General anaesthetic</div>

  <div class="copy abs" style="left:22px;top:92px;width:236px">
    <ul class="bullets">
      <li>Numbing liquid is injected around the nerves which supply your foot.</li>
      <li>The ankle block takes 5 - 10 minutes to perform and requires 4 - 5 injections.</li>
      <li>Approximately 10 - 20 minutes to make your foot numb to pain.</li>
      <li>I will check the ankle block is working before we start surgery using cold spray.</li>
      <li>Sensations of touch, pressure, vibration and movement will still be felt.</li>
      <li>I will use a screen so you can't see the surgery (unless you would like to see).</li>
      <li>Some patients bring headphones to block out the noise of the operation.</li>
    </ul>
  </div>

  <div class="copy abs" style="left:284px;top:92px;width:236px">
    <ul class="bullets">
      <li>I will perform the ankle block after I start the general anaesthetic.</li>
      <li>You should wake up from your surgery with a comfortable and numb foot/feet.</li>
      <li>If you wake in pain, we can repeat the ankle block or provide traditional painkillers.</li>
    </ul>
    <p style="margin-top:8px">Whatever you choose, there will be a cannula placed in your hand and heart and oxygen monitoring throughout.</p>
  </div>

  <div class="pill pill--round" style="left:284px;top:212px;width:236px">THE ALTERNATIVE</div>
  <div class="copy abs" style="left:284px;top:242px;width:236px">
    <ul class="bullets">
      <li>If you do not have an ankle block your surgery can still proceed.</li>
      <li>Post operative pain can be managed with traditional painkillers.</li>
      <li>However, you are more likely to need an overnight stay or feel sick after the anaesthetic.</li>
    </ul>
    <p style="margin-top:8px">If you have any further questions about an ankle block I will see you the day of your surgery. Alternatively, you can request the following optional services (as mentioned in my terms of business).</p>
  </div>

  <div class="pill" style="left:0;top:270px;width:258px">AFTER SURGERY</div>
  <div class="copy abs" style="left:22px;top:302px;width:262px">
    <p>You will go to the recovery area and then onto the ward when you are ready. It will be difficult to walk while the block is working so physiotherapists will help you first walk. If you need crutches they will teach you how to use them.</p>
    <p>Your foot will be numb and so you will not feel where your foot is in relation to nearby objects. As a result, it is easy to knock your foot. Please take extra care while your foot is still numb.</p>
    <p>As the block wears off, the foot may feel slightly painful, tingly or hot. At this point you should take your painkillers I have prescribed. Depending on your medical history you will have up to three painkillers. I would suggest to start with all three. You will also have an anti-sickness prescribed if one of the painkillers (typically codeine or morphine) makes you feel sick.</p>
    <p>Occasionally (1 - 2%), pain when the block wears off will be severe. In this case contact your surgeon's secretary. We can use stronger pain medication, but there will be a charge in writing and getting the private prescription to you (please see my terms of business) via courier.</p>
  </div>

  <div class="anatomy-visual" role="img" aria-label="Illustration of the bones of the foot and ankle with the ankle joint highlighted"></div>

  <svg class="abs" style="left:0;bottom:0" width="540" height="110" viewBox="0 0 540 110" aria-hidden="true">
    <path d="M0 46 L300 46 Q390 46 440 0 L540 0 L540 110 L0 110 Z" fill="var(--brand-blue)"/>
  </svg>
  <div class="footer" style="background:transparent;height:60px">© 2018 - Dr Tobias Wendell</div>
</section>

<section class="page page--overview">
  <div class="hero-photo" role="img" aria-label="Photograph of a person holding a painful ankle while wearing trainers"></div>
  <div class="clinic-mark"><span class="square"></span><span>THE<br>ASHBURY<br>CLINIC</span></div>

  <div class="pill pill--round" style="left:22px;top:186px;width:238px;justify-content:flex-start;padding-left:22px">ANKLE BLOCK</div>
  <div class="copy abs" style="left:22px;top:216px;width:238px">
    <p>You are scheduled to have surgery on your foot. It is my normal practice to offer and perform (with your consent) an ankle block. This is an optional injection of numbing liquid to the nerves which supply your foot. The ankle block can be performed when you are awake, sedated or under general anaesthesia.</p>
    <p>The ankle block can be combined with a general anaesthetic and with sedation. It can also be used to allow surgery to be performed with you wide awake in certain cases.</p>
    <p>Having or not having an ankle block does not change the pre operative fasting guidelines you have been given.</p>
    <p>There is a fee for performing an ankle block. Please consult my initial introductory email and terms of business for details.</p>
  </div>

  <div class="benefits">
    <h3>WHAT ARE THE BENEFITS</h3>
    <ol>
      <li>1 &nbsp;Excellent pain relief - usually 10 - 14 hours (and rarely 24 - 48 hours)</li>
      <li>2 &nbsp;Avoiding traditional painkillers which result in less post operative nausea and vomiting</li>
      <li>3 &nbsp;The option to avoid a general anaesthetic (if you wish)</li>
      <li>4 &nbsp;A faster recovery from the general anaesthetic</li>
      <li>5 &nbsp;Certain surgery requires an overnight stay in hospital without an ankle block</li>
    </ol>
  </div>

  <div class="pill pill--round" style="left:280px;top:186px;width:238px">WHAT ARE THE RISKS?</div>
  <div class="copy abs" style="left:280px;top:216px;width:238px">
    <p>As with all injections, there is the risk of bruising, bleeding and infection.</p>
    <p class="risk-heading">Nerve Damage</p>
    <ul class="bullets">
      <li>Occurs 1 in 5000 nerve blocks.</li>
      <li>Creates an area of numbness or weakness/paralysis in some/all the foot.</li>
      <li>Majority of nerve injuries will heal themselves within a year.</li>
      <li>There is no treatment to fix it.</li>
      <li>If the block has not worn off after 72 hours please let me know.</li>
    </ul>
    <p class="risk-heading">Failure</p>
    <ul class="bullets">
      <li>The success rate with ankle blocks is 98 - 99%.</li>
      <li>Some blocks will fail, partially or totally.</li>
      <li>If total failure, I will discuss repeating the block with your consent.</li>
    </ul>
    <p class="risk-heading">Pain during operation</p>
    <ul class="bullets">
      <li>If you choose to have wide awake surgery or surgery under sedation.</li>
      <li>The surgery will stop and I will discuss three options with you.</li>
      <li>More numbing liquid to be injected by the surgeon.</li>
      <li>More sedation / painkiller.</li>
      <li>Having a general anaesthetic.</li>
    </ul>
    <p style="margin-top:8px">If you decide to undergo surgery awake or sedated, there is a risk you will need to have a general anaesthetic if you feel pain. This is why the starvation instructions of awake surgery and general anaesthesia are the same.</p>
  </div>

  <div class="footer">© 2018 - Dr Tobias Wendell</div>
</section>

</body>
</html>
```